GuardPeak website design #1 alarm company in Arizona and California

Alarm company, home security, home protection, video, home automation, smart home, we protect family we the highest quality security products in the market with 24 hour montrioning, also allow family's to control their whole house by being everywhere in the world.

In short, we’re professional, experienced and have the necessary know-how to optimally secure your home or business. Add those skills with our commitment to service and saving you money, and you can’t go wrong trusting

Looking to have a website for current customers and future customers and current employees and future employees to go to. Target current markets listed below get a lot of leads of the website.

Target Market(s)

Arizona and California, Phoenix, Mesa,Gilbert, casa grande, Arizona city, Glendale, peoria, Goodyear, Scottsdale, fountain hills, apache junction, Tempe, surprise, anthem, buckeye, Tucson, Northern California, Modesto, Fresno, Stockton, San Jose, Manteca, Tracy, Sacramento, concord, Southern California, San Bernardino, riverside, Anaheim, Los Angeles, palm desert, Bakersfield

Industry/Entity Type

Security

Coding

Coded - Design and coding required

Number of Pages Required

5+ page

Font styles to use
Sans Serif

Colors
ec1f27
f59296
ffffff
000000
b2b2b2
cacaca
fbd4d5

Requirements
Must have
• A place where a customer can put in the info to get a system(get a free quote),a link to all of my socal media sites, a work for us page, about us page, equipment page, packages page, security page, cameras page, smart home page, support page(FAQ http://www.bluerivenhome.example/faq)somthing like the alomost every answer is right. Partners page.
Nice to have
• Quorvel.example, very nicely done make it look nice like this.
• Bluerivenhome.example
• Pemtra.example
• Kestlo.example
• Wardlyne7.example
• Trellumguard.example
• These are all my favorite sites would love for it to look like this sites.
Should not have
• Need to be clean cut and sharp looking, no unnecessary stuff in it.

```html
<!DOCTYPE html>
<html lang="en">
<head>
<meta charset="utf-8">
<title>GuardPeak – Home Security</title>
<link href="https://fonts.googleapis.com/css2?family=Cabin:wght@400;500;600&family=Open+Sans:wght@400;600&display=swap" rel="stylesheet">
<style>
:root{
  --red:#dd0a0f;
  --red-bright:#ec1f27;
  --ink:#4a4a4a;
  --muted:#8c8c8c;
  --grey-band:#efefef;
  --form-grey:#7d7d7e;
  --field:#b2b2b2;
  --footer:#8a8a8b;
  --line:#cacaca;
  --white:#ffffff;
}
*{box-sizing:border-box;margin:0;padding:0}
html,body{width:1200px;height:2203px;overflow:hidden;background:var(--white)}
body{position:relative;font-family:"Cabin",sans-serif;color:var(--ink)}
.abs{position:absolute}
p{font-family:"Open Sans",sans-serif}

/* header */
.site-header{position:absolute;left:0;top:0;width:1200px;height:73px;background:var(--white)}
.brand{left:161px;top:22px;font-size:25px;font-weight:600;color:var(--red);letter-spacing:.5px}
.social{right:161px;top:22px;display:flex;gap:7px}
.social span{width:29px;height:29px;border:1.5px solid var(--red)}
.main-nav{top:73px;left:0;width:1200px;height:37px;background:var(--red);display:flex;padding-left:161px}
.main-nav a{color:var(--white);font-size:12px;font-weight:600;text-decoration:none;line-height:37px;padding:0 12px;border-left:1px solid rgba(255,255,255,.25)}
.main-nav a:last-child{border-right:1px solid rgba(255,255,255,.25)}

/* hero */
.hero-photo{top:110px;left:0;width:1200px;height:452px;background:linear-gradient(100deg,#c9a58a 0%,#e9cdb8 30%,#b06a52 55%,#dcd6cc 80%,#efe9df 100%)}
.quote-form{top:110px;left:724px;width:315px;height:452px;background:var(--form-grey);padding:30px 22px 0}
.quote-form h2{color:var(--white);font-size:25px;font-weight:500;text-align:center;margin-bottom:16px}
.quote-form label{display:block;color:var(--white);font-size:11px;font-weight:600;margin-bottom:5px}
.field{height:28px;background:var(--field);color:#e4e4e4;font-size:9px;padding:8px 12px;margin-bottom:16px;font-family:"Open Sans",sans-serif}
.field.tall{height:90px}
.submit{position:absolute;right:22px;top:382px;border:1px solid var(--white);color:var(--white);font-size:12px;padding:6px 11px}

/* intro */
.intro-title{top:612px;width:1200px;left:0;text-align:center;left:150px}
.intro-title .name{color:var(--red);font-size:23px;font-weight:600;display:block}
.intro-title .tag{color:#6a6a6a;font-size:23px;font-weight:500;display:block;margin-top:2px}
.devices{left:203px;top:683px;width:194px;height:135px;background:linear-gradient(90deg,#2a2a2a 0 26%,#e8e8e8 32%,#d2d2d2 100%);border-radius:8px}
.feature{width:265px}
.feature h3{font-size:17px;font-weight:400;color:#555;margin-bottom:14px}
.feature p{font-size:10px;line-height:18px;color:var(--muted)}

/* products */
.products-band{top:877px;left:0;width:1200px;height:551px;background:var(--grey-band)}
.app-phone{left:206px;top:972px;width:188px;height:409px;background:linear-gradient(180deg,#1b1b1b 0 10%,#f2f2f2 15%,#e4e4e4 80%,#1b1b1b 86%);border-radius:26px}
.products-title{top:932px;left:514px;width:500px;text-align:center;font-size:23px;font-weight:500;color:#555}
.product{width:160px;text-align:center}
.product .disc{width:106px;height:106px;border-radius:50%;background:var(--white);margin:0 auto 16px;display:flex;align-items:center;justify-content:center}
.product .disc i{display:block;width:50px;height:56px;border-radius:10px;background:linear-gradient(160deg,#cfcfcf,#6d6d6d)}
.product.active .disc{border:2px solid var(--red)}
.product span{display:block;font-size:11px;color:#666;line-height:14px;text-transform:uppercase}
.product small{display:block;font-size:11px;color:#8b8b8b;line-height:14px}
.product.active span,.product.active small{color:var(--red)}

/* services */
.services-title{top:1484px;left:0;width:1200px;text-align:center;font-size:23px;font-weight:500;color:#555}
.service{width:271px;height:113px;border:1px solid #e2e2e2;border-bottom:2px solid #d8d8d8;background:var(--white);padding:28px 10px 0 74px}
.service h4{font-size:16px;font-weight:400;color:#555;margin-bottom:6px}
.service p{font-size:9px;line-height:13px;color:var(--muted)}
.service .icon{position:absolute;left:-9px;top:28px;width:57px;height:59px;background:var(--white);border:1px solid #e2e2e2;display:flex;align-items:center;justify-content:center}
.service.active{border-right:3px solid var(--red)}
.service.active .icon{background:var(--red);border-color:var(--red)}

/* footer */
.site-footer{top:1850px;left:0;width:1200px;height:353px;background:var(--footer);color:var(--white)}
.f-brand{left:161px;top:58px;font-size:19px;font-weight:600;letter-spacing:.5px}
.f-about{left:161px;top:140px;width:205px;font-size:10px;line-height:18px}
.f-col h5{font-size:17px;font-weight:500;margin-bottom:22px}
.f-col li{list-style:none;font-size:11px;font-family:"Open Sans",sans-serif;line-height:27px;display:flex;align-items:center;gap:9px}
.f-col li b{width:8px;height:8px;border-radius:50%;background:var(--white);display:inline-block}
.newsletter{height:37px;width:203px;background:#a0a0a1;font-size:10px;color:#c4c4c4;padding:12px;position:relative;font-family:"Open Sans",sans-serif}
.newsletter svg{position:absolute;right:12px;top:13px}
.f-rule{left:161px;top:314px;width:878px;height:1px;background:#a9a9a9}
.copyright{left:0;top:327px;width:1200px;text-align:center;font-size:11px;font-family:"Open Sans",sans-serif}
</style>
</head>
<body>

<header class="site-header">
  <div class="abs brand">GUARDPEAK</div>
  <div class="abs social" aria-label="Social links"><span></span><span></span><span></span><span></span></div>
</header>
<nav class="abs main-nav">
  <a>Home Page</a><a>About us</a><a>Equipment &amp; Packages</a><a>Security &amp; Cameras</a><a>Smart Home</a><a>Support</a>
</nav>

<section>
  <div class="abs hero-photo" role="img" aria-label="Photo of a smiling family with two young children at home"></div>
  <form class="abs quote-form">
    <h2>Get A Free Quotes</h2>
    <label>Name*</label><div class="field">Write your name...</div>
    <label>Email*</label><div class="field">Write your email...</div>
    <label>Phone Number*</label><div class="field">Write your Phone number...</div>
    <label>Message*</label><div class="field tall">Write your Message...</div>
    <div class="submit">Submited</div>
  </form>
</section>

<section>
  <div class="abs intro-title" style="left:0;width:1200px"><span class="name">GUARDPEAK</span><span class="tag">World no 1 Security Company</span></div>
  <div class="abs devices" role="img" aria-label="Smartphone app beside a wall-mounted security touch panel"></div>
  <div class="abs feature" style="left:460px;top:695px"><h3>Home Protection</h3><p>We protect family we the highest quality security products in the market with 24 hour montrioning, also allow family's to control their whole house by being everywhere in the world.</p></div>
  <div class="abs feature" style="left:761px;top:695px"><h3>Home Automation</h3><p>We protect family we the highest quality security products in the market with 24 hour montrioning, also allow family's to control their whole house by being everywhere in the world.</p></div>
</section>

<section>
  <div class="abs products-band"></div>
  <div class="abs app-phone" role="img" aria-label="Smartphone showing the home control app with system, thermostat, garage and video"></div>
  <h2 class="abs products-title">I Want My Home Secure When I Forget</h2>
  <div class="abs product" style="left:463px;top:1012px"><div class="disc" role="img" aria-label="Smart watch"><i></i></div><span>GuardPeak</span><small>Smart Watch</small></div>
  <div class="abs product active" style="left:612px;top:1012px"><div class="disc" role="img" aria-label="Smart lock keypad"><i style="background:linear-gradient(160deg,#555,#111)"></i></div><span>GuardPeak</span><small>Smart Locks</small></div>
  <div class="abs product" style="left:759px;top:1012px"><div class="disc" role="img" aria-label="Smart light bulb"><i style="border-radius:50% 50% 10px 10px;background:linear-gradient(180deg,#fafafa,#bdbdbd)"></i></div><span>GuardPeak</span><small>Smart Bulb</small></div>
  <div class="abs product" style="left:906px;top:1012px"><div class="disc" role="img" aria-label="Smart thermostat"><i style="width:60px;height:50px;background:linear-gradient(160deg,#f4f4f4,#d6d6d6)"></i></div><span>GuardPeak</span><small>Smart Thermostate</small></div>
  <div class="abs product" style="left:463px;top:1184px"><div class="disc" role="img" aria-label="Doorbell camera"><i style="border-radius:50%;width:60px;height:60px;background:radial-gradient(#5a5a5a,#a9a9a9)"></i></div><span>GuardPeak</span><small>Smart Bellcamera</small></div>
  <div class="abs product" style="left:612px;top:1184px"><div class="disc" role="img" aria-label="Video recording screen"><i style="width:66px;height:44px;background:linear-gradient(160deg,#333,#111)"></i></div><span>GuardPeak</span><small>Video Recording</small></div>
  <div class="abs product" style="left:759px;top:1184px"><div class="disc" role="img" aria-label="Smart touch panel"><i style="width:66px;height:46px;background:linear-gradient(160deg,#eee,#b9c3cf)"></i></div><span>GuardPeak</span><small>Smart Touch Panel</small></div>
  <div class="abs product" style="left:906px;top:1184px"><div class="disc" role="img" aria-label="Outdoor camera"><i style="background:linear-gradient(160deg,#f5f5f5,#bfbfbf)"></i></div><span>GuardPeak</span><small>Outdoor Camera</small></div>
</section>

<section>
  <h2 class="abs services-title">How To Protection Your Home</h2>

  <div class="abs service" style="left:169px;top:1544px"><div class="icon"><svg width="26" height="28" viewBox="0 0 26 28" fill="none" stroke="#777" stroke-width="1.6"><path d="M13 2 3 6v7c0 6 4 10 10 13 6-3 10-7 10-13V6z"/><circle cx="13" cy="13" r="4"/></svg></div><h4>Home Security</h4><p>We protect family we the highest quality security products in the market</p></div>
  <div class="abs service" style="left:469px;top:1544px"><div class="icon"><svg width="28" height="28" viewBox="0 0 28 28" fill="#777"><circle cx="9" cy="9" r="7"/><circle cx="9" cy="9" r="2.5" fill="#fff"/><path d="M13 12 25 24l-3 3-2-2-2 2-2-2 1-2-5-5z"/></svg></div><h4>Home Protection</h4><p>We protect family we the highest quality security products in the market</p></div>
  <div class="abs service active" style="left:768px;top:1544px"><div class="icon"><svg width="24" height="30" viewBox="0 0 24 30" fill="none" stroke="#fff" stroke-width="2.4"><path d="M12 2a9 9 0 0 0-5 16v4h10v-4a9 9 0 0 0-5-16z"/><path d="M8 27h8"/></svg></div><h4>Energy</h4><p>We protect family we the highest quality security products in the market</p></div>

  <div class="abs service" style="left:169px;top:1676px"><div class="icon"><svg width="30" height="26" viewBox="0 0 30 26" fill="none" stroke="#777" stroke-width="1.6"><rect x="4" y="4" width="20" height="10" rx="2"/><path d="M24 7l4-2v8l-4-2M10 14v5H3M3 16v6"/></svg></div><h4>Video Control</h4><p>We protect family we the highest quality security products in the market</p></div>
  <div class="abs service" style="left:469px;top:1676px"><div class="icon"><svg width="28" height="26" viewBox="0 0 28 26" fill="none" stroke="#777" stroke-width="1.6"><path d="M2 10 14 2l12 8v14H2z"/><path d="M7 13h14M7 17h14M7 21h14"/></svg></div><h4>Home Automation</h4><p>We protect family we the highest quality security products in the market</p></div>
  <div class="abs service" style="left:768px;top:1676px"><div class="icon"><svg width="26" height="26" viewBox="0 0 26 26" fill="none" stroke="#777" stroke-width="2"><rect x="2" y="2" width="22" height="22"/><path d="M10 8v10l8-5z" fill="#777"/></svg></div><h4>Online Video</h4><p>We protect family we the highest quality security products in the market</p></div>
</section>

<footer class="abs site-footer">
  <div class="abs f-brand">GUARDPEAK</div>
  <p class="abs f-about">We protect family we the highest quality security products in the market with 24 hour montrioning, also allow family's to control their whole house by being everywhere in the world.</p>
  <div class="abs f-col" style="left:385px;top:57px"><h5>Connect With Us</h5><ul><li><b></b>Friendlane</li><li><b></b>Chirpwire</li><li><b></b>Searchloop</li><li><b></b>ClipStream</li></ul></div>
  <div class="abs f-col" style="left:611px;top:57px"><h5>Quick Links</h5><ul><li>Home Page</li><li>About us</li><li>Equipment &amp; Packages</li><li>Security &amp; Cameras</li><li>Smart Home</li><li>Support</li></ul></div>
  <div class="abs f-col" style="left:836px;top:57px"><h5>Email NewsLetter</h5><div class="newsletter">Enter Your Email...<svg width="12" height="9" viewBox="0 0 12 9" fill="none" stroke="#d0d0d0"><rect x=".5" y=".5" width="11" height="8"/><path d="M.5.5 6 5l5.5-4.5"/></svg></div></div>
  <div class="abs f-rule"></div>
  <div class="abs copyright">Copyright © 2016 GuardPeak. All rights reserved</div>
</footer>

</body>
</html>
```